Harvest Ledger Group
Business Cards, Envelopes and Letterhead
Project: Harvest Ledger Group
Harvest Ledger Group -
Creative Brief
Bright & Fun-filled
Marcus T. Halvorsen
President
47 Brookmere Loop West, Suite B318 Englewood, CO 80214
mh@harvestledgergroup.com
www.harvestledgergroup.com

```html
<!DOCTYPE html>
<html lang="en">
<head>
<meta charset="utf-8">
<title>Harvest Ledger Group – Stationery Set</title>
<link href="https://fonts.googleapis.com/css2?family=Libre+Baskerville:wght@700&family=Open+Sans:wght@400;600&display=swap" rel="stylesheet">
<style>
  :root{
    --bg-light:#b4b6b9;
    --bg-dark:#7c7e82;
    --paper:#ffffff;
    --brand-blue:#2a6fc1;
    --brand-navy:#1c3f74;
    --wave-grey:#c9cdd3;
    --text-grey:#5b5f66;
    --faint-blue:#dfe9f6;
    --line-grey:#d7d9dc;
  }
  *{box-sizing:border-box;margin:0;padding:0}
  html,body{width:1200px;height:626px;overflow:hidden}
  body{
    position:relative;
    background:radial-gradient(ellipse at 50% 45%,var(--bg-light) 0%,var(--bg-dark) 100%);
    font-family:"Open Sans",Arial,sans-serif;
    color:var(--text-grey);
  }
  .sheet{position:absolute;background:var(--paper);overflow:hidden;box-shadow:0 1px 3px rgba(0,0,0,.25)}
  .card{border-radius:6px;width:187px;height:105px;left:34px}
  .card--front{top:199px}
  .card--back{top:319px}
  .letterhead{left:233px;top:36px;width:403px;height:564px}
  .envelope{left:679px;width:492px;height:257px}
  .envelope--back{top:36px}
  .envelope--front{top:312px}

  .brand{display:flex;flex-direction:column;align-items:center;gap:3px}
  .brand__mark{background:var(--brand-blue)}
  .brand__name{font-family:"Libre Baskerville",Georgia,serif;font-weight:700;color:var(--brand-navy);text-transform:uppercase;letter-spacing:.3px;white-space:nowrap}

  .card--front .brand{position:absolute;left:0;right:0;top:22px}
  .card--front .brand__mark{width:22px;height:22px}
  .card--front .brand__name{font-size:6.5px}

  .card--back .brand{position:absolute;left:14px;top:12px}
  .card--back .brand__mark{width:14px;height:14px}
  .card--back .brand__name{font-size:4.6px}
  .card__details{position:absolute;right:10px;top:12px;text-align:right;font-size:4px;line-height:1.45}
  .card__name{font-weight:600;font-size:5px;color:var(--brand-navy)}

  .wave{position:absolute;left:0;bottom:0;width:100%}

  .letterhead .brand{position:absolute;left:22px;top:20px}
  .letterhead .brand__mark{width:26px;height:26px}
  .letterhead .brand__name{font-size:6.5px}
  .letterhead__rule{position:absolute;left:22px;top:62px;width:84px;height:1px;background:var(--line-grey)}
  .letterhead__watermark{position:absolute;left:105px;top:190px;width:190px;height:190px;background:var(--faint-blue)}

  .contact{position:absolute;font-size:4.3px;line-height:1.5;display:grid;grid-template-columns:auto auto;column-gap:22px}
  .letterhead .contact{left:14px;bottom:8px}
  .envelope--front .contact{left:16px;top:150px}

  .envelope--front .brand{position:absolute;left:0;right:0;top:62px}
  .envelope--front .brand__mark{width:26px;height:26px}
  .envelope--front .brand__name{font-size:7px}
</style>
</head>
<body>

<div class="sheet card card--front">
  <div class="brand"><span class="brand__mark"></span><span class="brand__name">Harvest Ledger Group</span></div>
</div>

<div class="sheet card card--back">
  <div class="brand"><span class="brand__mark"></span><span class="brand__name">Harvest Ledger Group</span></div>
  <div class="card__details">
    <div class="card__name">Marcus T. Halvorsen</div>
    <div>President</div>
    <div>P (720) 555-0148</div>
    <div>C (303) 555-0192</div>
    <div>F (720) 555-0163</div>
    <div>mh@harvestledgergroup.com</div>
  </div>
  <svg class="wave" viewBox="0 0 400 90" height="42" preserveAspectRatio="none" aria-hidden="true">
    <path d="M0 40 C120 75 250 5 400 12 L400 28 C250 20 120 88 0 56Z" fill="var(--wave-grey)"/>
    <path d="M0 56 C120 88 250 20 400 28 L400 90 L0 90Z" fill="var(--brand-blue)"/>
  </svg>
</div>

<div class="sheet letterhead">
  <div class="brand"><span class="brand__mark"></span><span class="brand__name">Harvest Ledger Group</span></div>
  <div class="letterhead__rule"></div>
  <div class="letterhead__watermark" role="img" aria-label="Faint brand square"></div>
  <svg class="wave" viewBox="0 0 400 90" height="78" preserveAspectRatio="none" aria-hidden="true" style="bottom:26px">
    <path d="M0 40 C120 75 250 5 400 12 L400 28 C250 20 120 88 0 56Z" fill="var(--wave-grey)"/>
    <path d="M0 56 C120 88 250 20 400 28 L400 90 L0 90Z" fill="var(--brand-blue)"/>
  </svg>
  <div class="contact">
    <span>P (720) 555-0148</span><span>mh@harvestledgergroup.com</span>
    <span>C (303) 555-0192</span><span>www.harvestledgergroup.com</span>
    <span>F (720) 555-0163</span><span>47 Brookmere Loop West, Suite B318 Englewood, CO 80214</span>
  </div>
</div>

<div class="sheet envelope envelope--back">
  <svg width="492" height="257" viewBox="0 0 492 257" aria-hidden="true">
    <polyline points="0,48 246,165 492,48" fill="none" stroke="var(--line-grey)" stroke-width="1"/>
    <line x1="0" y1="48" x2="492" y2="48" stroke="var(--line-grey)" stroke-width="1"/>
  </svg>
</div>

<div class="sheet envelope envelope--front">
  <div class="brand"><span class="brand__mark"></span><span class="brand__name">Harvest Ledger Group</span></div>
  <div class="contact">
    <span>P (720) 555-0148</span><span>mh@harvestledgergroup.com</span>
    <span>C (303) 555-0192</span><span>www.harvestledgergroup.com</span>
    <span>F (720) 555-0163</span><span>47 Brookmere Loop West, Suite B318 Englewood, CO 80214</span>
  </div>
  <svg class="wave" viewBox="0 0 400 90" height="70" preserveAspectRatio="none" aria-hidden="true">
    <path d="M0 40 C120 75 250 5 400 12 L400 28 C250 20 120 88 0 56Z" fill="var(--wave-grey)"/>
    <path d="M0 56 C120 88 250 20 400 28 L400 90 L0 90Z" fill="var(--brand-blue)"/>
  </svg>
</div>

</body>
</html>
```